My Billboard for Law Firm

Designing a billboard

Should have
Corvell & Pine, LLC
Ph: 555-214-7390
Auto Accidents / Personal Injury
Family Law
Criminal Defense
Real Estate
Free Consultation

Target Market(s)

Legal

Industry/Entity Type

Legal

Font styles to use
Serif
Sans Serif

Requirements
Must have
• Designing a billboard

Should have
Corvell & Pine, LLC
Ph: 555-214-7390
Family Law
Criminal Defense
Real Estate
Free Consultation
Nice to have
• Nice to have info above
Should not have
• None

```html
<!DOCTYPE html>
<html lang="en">
<head>
<meta charset="utf-8">
<title>Corvell &amp; Pine, LLC Billboard</title>
<link href="https://fonts.googleapis.com/css2?family=Gelasio:wght@400;500&family=Montserrat:wght@600&display=swap" rel="stylesheet">
<style>
  :root {
    --frame: #5e3b26;
    --cream: #f3ecd8;
    --cream-edge: #eee4c8;
    --slate: #3e4a50;
    --ink: #141414;
    --gold: #927936;
    --gold-shadow: #533a07;
    --footer-ink: #686050;
    --photo-dark: #2a2026;
    --photo-mid: #4a3036;
    --photo-warm: #5a2c1c;
  }
  html, body { margin: 0; padding: 0; overflow: hidden; }
  body { width: 1200px; height: 521px; background: var(--frame); }
  .billboard {
    position: relative;
    width: 1200px; height: 521px;
    background: var(--frame);
    overflow: hidden;
  }
  .masthead {
    position: absolute; left: 9px; top: 9px; width: 1182px; height: 124px;
    background: linear-gradient(90deg, var(--cream-edge), var(--cream) 40%, var(--cream) 70%, var(--cream-edge));
  }
  .firm-name {
    position: absolute; left: 0; width: 100%; top: 10px;
    margin: 0; text-align: center;
    font-family: "Gelasio", Georgia, serif; font-weight: 400;
    font-size: 76px; line-height: 1; color: var(--slate);
    letter-spacing: 1px; padding-left: 22px; box-sizing: border-box;
  }
  .attorneys {
    position: absolute; left: 0; width: 100%; top: 86px;
    margin: 0; text-align: center;
    font-family: "Gelasio", Georgia, serif; font-size: 33px; line-height: 1;
    color: var(--ink); padding-left: 22px; box-sizing: border-box;
  }
  .backdrop {
    position: absolute; left: 9px; top: 133px; width: 1182px; height: 307px;
    background:
      radial-gradient(ellipse at 18% 55%, var(--photo-mid), transparent 60%),
      linear-gradient(90deg, var(--photo-dark) 0%, var(--photo-mid) 35%, var(--photo-warm) 70%, #4a2418 100%);
  }
  .practice-shadows { position: absolute; left: 0; top: 0; }
  .practice {
    position: absolute; box-sizing: border-box;
    background: var(--gold); color: #fff;
    font-family: "Gelasio", Georgia, serif; font-size: 41px; line-height: 1;
    display: flex; align-items: center; justify-content: center;
    white-space: nowrap;
  }
  .practice--injury { left: 273px; top: 145px; width: 663px; height: 68px; }
  .practice--family { left: 482px; top: 216px; width: 245px; height: 67px; }
  .practice--criminal { left: 441px; top: 287px; width: 326px; height: 67px; }
  .practice--estate { left: 489px; top: 357px; width: 238px; height: 67px; }
  .footer {
    position: absolute; left: 9px; top: 440px; width: 1182px; height: 72px;
    background: var(--cream);
    display: flex; align-items: center; justify-content: center;
    font-family: "Montserrat", Arial, sans-serif; font-weight: 600;
    font-size: 32px; color: var(--footer-ink); white-space: nowrap;
  }
  .footer .sep { margin: 0 22px; }
</style>
</head>
<body>
<div class="billboard">
  <header class="masthead">
    <h1 class="firm-name">Corvell &amp; Pine, LLC</h1>
    <p class="attorneys">Attorneys: Miles Corvell, &amp; Daniel R. Pine</p>
  </header>

  <div class="backdrop" role="img" aria-label="Photograph of brass scales of justice beside a polished wooden desk"></div>

  <svg class="practice-shadows" width="1200" height="521" viewBox="0 0 1200 521" aria-hidden="true">
    <polygon points="273,213 936,213 727,283 482,283" fill="var(--gold-shadow)"/>
    <polygon points="451,357 767,357 727,424 489,424" fill="var(--gold-shadow)"/>
  </svg>

  <div class="practice practice--injury">Auto Accidents / Personal Injury</div>
  <div class="practice practice--family">Family Law</div>
  <div class="practice practice--criminal">Criminal Defense</div>
  <div class="practice practice--estate">Real Estate</div>

  <footer class="footer">
    <span>Free Consultation</span><span class="sep">-</span>
    <span>Ph: 555-214-7390</span><span class="sep">-</span>
    <span>www.corvellpinelaw.net</span>
  </footer>
</div>
</body>
</html>
```